CoinHarbor Rangers (Ledger Meadow)
A website dedicated to crypto education. We are a new company focused on blockchain edutainment (education and interesting and entertaining content about the blockchain space). We want a fun, clean/minimalist and modern website that is made up of an education platform which could be a website in it’s own right. It will be the reference point for our users/community for all of our other blockchain based content in the CHR website ecosystem which will be covering; crypto news, digital asset investing (including a technical and fundamental analysis subscription service), blockchain business solutions and an NFT section that will cover creative art projects (art, music, gaming and more). To feature a logins and payment system which may need a shopping basket set up for tutorial/educational platform that is accessed via the website, NFT page with sub-categories: education and NFT and metaverse/virtual world and merchandise shopping page which is Web 3.0 enabled (able to link to a VaultPorch, Keel Purse etc , digital asset education page featuring blog and newsletter subscriptions links, A social media page where people can access videos, podcasts and our presence on other platforms such as Chirpline, Snapmosaic, Hubbleroom, Wirepost etc.
Number of Pages Required
5+ page

```html
<!DOCTYPE html>
<html lang="en">
<head>
<meta charset="utf-8">
<title>CoinHarbor Rangers</title>
<link href="https://fonts.googleapis.com/css2?family=Anton&family=Space+Mono:wght@400;700&family=Poppins:wght@400;600&display=swap" rel="stylesheet">
<style>
:root{
  --night:#130f35;
  --plum:#1d0f45;
  --violet:#5a2fa0;
  --footer:#4d2785;
  --ink:#1a0a3c;
  --accent-text:#3a1590;
  --white:#ffffff;
  --mist:#eef2f7;
  --yellow:#f5fb14;
  --slide-blue:#4f86c6;
  --slide-red:#c8001f;
}
*{box-sizing:border-box;margin:0;padding:0}
html,body{width:1200px;height:3546px;overflow:hidden}
body{position:relative;background:var(--night);color:var(--white);font-family:"Space Mono",monospace}
section,header,footer{position:absolute;left:0;width:1200px}
.abs{position:absolute}
.display{font-family:"Anton",sans-serif;letter-spacing:.3px;font-weight:400}
h1,h2{font-weight:400}

/* hero */
.hero{top:0;height:595px;background:linear-gradient(100deg,#1a1240 0%,#141036 55%,#0c0b22 100%)}
.logo{left:111px;top:16px;font-size:26px}
.nav-links{left:431px;top:24px;display:flex;gap:24px;font-size:17px}
.pill-outline{border:2px solid var(--white);border-radius:30px;display:flex;align-items:center;justify-content:center;font-size:15px}
.btn-register{left:793px;top:14px;width:131px;height:44px}
.btn-community{left:944px;top:14px;width:131px;height:44px}
.hero-title{left:111px;top:196px;font-size:48px}
.hero-text{left:111px;top:282px;width:470px;font-family:"Anton",sans-serif;font-size:16px;line-height:26px}
.btn-start{left:111px;top:394px;width:157px;height:50px;background:var(--white);color:var(--ink);border-radius:30px;display:flex;align-items:center;justify-content:center;font-family:"Anton",sans-serif;font-size:16px}
.hero-art{left:680px;top:92px;width:470px;height:440px;border-radius:50%;background:radial-gradient(circle at 50% 50%,#3a1f86 0%,#2a1567 40%,rgba(30,18,70,.4) 60%,rgba(20,16,54,0) 72%)}

/* education */
.education{top:595px;height:413px;background:linear-gradient(180deg,#fff 0%,#fff 55%,var(--mist) 100%);color:var(--ink);text-align:center}
.section-title{width:100%;font-size:34px;letter-spacing:3px}
.education .section-title{top:56px}
.edu-text{left:165px;width:870px;top:124px;font-size:17px;line-height:26px}
.btn-fill{background:var(--ink);color:var(--white);border-radius:30px;display:flex;align-items:center;justify-content:center;font-size:19px}
.btn-line{border:2px solid var(--ink);color:var(--ink);border-radius:30px;display:flex;align-items:center;justify-content:center;font-size:19px}
.btn-signup{left:413px;top:278px;width:177px;height:59px}
.btn-blog{left:610px;top:278px;width:177px;height:59px}

/* ecosystem */
.ecosystem{top:1008px;height:603px;background:linear-gradient(180deg,#1d0f45 0%,#150c38 60%,#0e0b2a 100%);text-align:center}
.ecosystem .section-title{top:70px;letter-spacing:4px;word-spacing:14px}
.eco-card{top:162px;width:224px}
.eco-thumb{width:224px;height:223px;border-radius:26px}
.eco-label{margin-top:26px;font-size:28px;line-height:26px;letter-spacing:2px}

/* nft education */
.nft-edu{top:1611px;height:578px;background:linear-gradient(180deg,#f4f7fb 0%,#e8eef5 100%);text-align:center}
.nft-edu .section-title{top:60px;color:var(--accent-text)}
.nft-text{left:160px;width:880px;top:130px;font-size:16px;line-height:26px;color:var(--accent-text)}
.slide{top:226px;width:471px;height:270px;border-radius:28px}
.slide-blue{left:111px;background:linear-gradient(90deg,var(--slide-blue) 0%,#e0a98a 55%,var(--slide-blue) 100%)}
.slide-red{left:614px;background:linear-gradient(90deg,#9fd420 0%,#7a6a3a 30%,var(--slide-red) 55%,var(--slide-red) 100%)}
.arrow{top:360px;width:24px;height:34px}

/* tutorial */
.tutorial{top:2189px;height:878px;background:linear-gradient(180deg,#1a1040 0%,#120d33 60%,#0e0b2b 100%);text-align:center}
.tutorial .section-title{top:82px;font-size:26px;letter-spacing:2px}
.tab{top:154px;width:161px;height:51px;border-radius:30px;display:flex;align-items:center;justify-content:center;font-size:19px}
.tab-videos{left:430px;background:var(--violet)}
.tab-podcast{left:610px;border:2px dashed var(--violet)}
.video{left:111px;top:261px;width:978px;height:448px;border-radius:30px;background:linear-gradient(90deg,var(--yellow) 0%,#c98a6a 25%,#b8614a 40%,var(--yellow) 55%,#8a1a10 75%,var(--yellow) 100%);overflow:hidden}
.play{left:445px;top:160px;width:88px;height:88px;border-radius:50%;background:var(--white)}
.price-pill{top:746px;height:44px;border-radius:24px;background:var(--violet);display:flex;align-items:center;justify-content:center;font-size:19px}
.social-row{display:flex;gap:8px}
.social-chip{height:30px;padding:0 9px;border:1.5px solid var(--white);border-radius:15px;display:flex;align-items:center;font-size:11px;white-space:nowrap}

/* footer */
.site-footer{top:3067px;height:479px;background:var(--footer);text-align:center}
.footer-logo{width:100%;top:70px;font-size:26px}
.footer-nav{width:100%;top:134px;display:flex;justify-content:center;gap:40px;font-size:30px}
.footer-social{width:100%;top:214px;justify-content:center}
.partner{top:300px;height:60px;display:flex;align-items:center;gap:14px;font-size:32px;letter-spacing:6px}
.partner-mark{width:54px;height:54px;background:#f0a060;border-radius:50%}
.partner-mark.square{border-radius:6px;background:transparent;border:4px solid var(--white);width:48px;height:54px}
.cards{left:738px;top:310px;display:flex;gap:6px}
.card{width:52px;height:34px;background:var(--white);border-radius:4px;color:var(--footer);font-size:8px;display:flex;align-items:center;justify-content:center;font-weight:700;text-align:center;line-height:9px}
.footer-rule{left:111px;top:389px;width:978px;height:1px;background:rgba(255,255,255,.7)}
.copyright{width:100%;top:418px;font-family:"Poppins",sans-serif;font-weight:600;font-size:14px}
</style>
</head>
<body>

<header class="hero">
  <div class="abs logo display">CoinHarbor Rangers</div>
  <nav class="abs nav-links"><span>Home</span><span>About Us</span><span>NFT</span><span>Contact</span></nav>
  <div class="abs pill-outline btn-register">Register</div>
  <div class="abs pill-outline btn-community">Community</div>
  <h1 class="abs hero-title display">CoinHarbor Rangers</h1>
  <p class="abs hero-text">Nemo enim ipsam voluptatem quia voluptas sit aspernatur aut odit aut fugit, sed quia consequuntur magni dolores eos qui ratione vipsum quia dolor sit amet, consectetur</p>
  <div class="abs btn-start">Get Started</div>
  <div class="abs hero-art" role="img" aria-label="Pixel-art blue character with orange ears and two small white ghosts on a purple circle"></div>
</header>

<section class="education">
  <h2 class="abs section-title">Digital Asset Education</h2>
  <p class="abs edu-text">Sed ut perspiciatis unde omnis iste natus error sit voluptatem accusantium doloremque laudantium, totam rem aperiam, eaque ipsa quae ab illo inventore veritatis et quasi architecto beatae vitae dicta sunt explicabo. Nemo enim ipsam voluptatem quia voluptas sit aspernatur aut odit aut fugit, sed quia consequuntur magni dolores eos qui ratione voluptatem</p>
  <div class="abs btn-fill btn-signup">Signup</div>
  <div class="abs btn-line btn-blog">Blog</div>
</section>

<section class="ecosystem">
  <h2 class="abs section-title">CHR ecosystem</h2>
  <div class="abs eco-card" style="left:111px">
    <div class="eco-thumb" role="img" aria-label="Pixel-art NFT banner with a row of characters" style="background:linear-gradient(180deg,#e8a040 0%,#8a4a4a 50%,#4a3a3a 100%)"></div>
    <div class="eco-label">Crypto news</div>
  </div>
  <div class="abs eco-card" style="left:362px">
    <div class="eco-thumb" role="img" aria-label="Pixel-art character on a teal background" style="background:linear-gradient(135deg,#3f8e99,#2f6f78)"></div>
    <div class="eco-label">Digital asset investing</div>
  </div>
  <div class="abs eco-card" style="left:613px">
    <div class="eco-thumb" role="img" aria-label="Pixel-art character with red mohawk on a purple background" style="background:linear-gradient(135deg,#4a1a9a,#3a0f80)"></div>
    <div class="eco-label">Blockchain business solutions</div>
  </div>
  <div class="abs eco-card" style="left:864px">
    <div class="eco-thumb" role="img" aria-label="Pixel-art character with 3D glasses on a blue background" style="background:linear-gradient(135deg,#5a8ad0,#4a7cc4)"></div>
    <div class="eco-label">NFT art</div>
  </div>
</section>

<section class="nft-edu">
  <h2 class="abs section-title">NFT education</h2>
  <p class="abs nft-text">Sed ut perspiciatis unde omnis iste natus error sit voluptatem accusantium doloremque laudantium, totam rem aperiam, eaque ipsa quae ab</p>
  <svg class="abs arrow" style="left:68px" viewBox="0 0 24 34"><path d="M17 4 L6 17 L17 30" fill="none" stroke="#1a0a3c" stroke-width="3"/></svg>
  <div class="abs slide slide-blue" role="img" aria-label="Close-up pixel-art character with 3D glasses on blue"></div>
  <div class="abs slide slide-red" role="img" aria-label="Close-up pixel-art character with green hood and purple glasses on red"></div>
  <svg class="abs arrow" style="left:1107px" viewBox="0 0 24 34"><path d="M7 4 L18 17 L7 30" fill="none" stroke="#1a0a3c" stroke-width="3"/></svg>
</section>

<section class="tutorial">
  <h2 class="abs section-title">CoinHarbor Tutorial</h2>
  <div class="abs tab tab-videos">Videos</div>
  <div class="abs tab tab-podcast">Podacst</div>
  <div class="abs video" role="img" aria-label="Video cover: pixel-art character beside large NFT lettering on yellow">
    <div class="abs play">
      <svg width="88" height="88" viewBox="0 0 88 88"><path d="M38 33 L56 44 L38 55 Z" fill="#5a2fa0"/></svg>
    </div>
  </div>
  <div class="abs price-pill" style="left:378px;width:112px">Free</div>
  <div class="abs price-pill" style="left:507px;width:112px">Paid</div>
  <div class="abs social-row" style="left:636px;top:753px">
    <span class="social-chip">Facelane</span><span class="social-chip">Chirpline</span><span class="social-chip">Linkroster</span><span class="social-chip">Hubbleroom</span>
  </div>
</section>

<footer class="site-footer">
  <div class="abs footer-logo display">CoinHarbor Rangers</div>
  <nav class="abs footer-nav"><span>Home</span><span>About Us</span><span>NFT</span><span>Contact</span></nav>
  <div class="abs social-row footer-social">
    <span class="social-chip">Facelane</span><span class="social-chip">Chirpline</span><span class="social-chip">Linkroster</span><span class="social-chip">Hubbleroom</span>
  </div>
  <div class="abs partner" style="left:111px"><span class="partner-mark"></span>VaultPorch</div>
  <div class="abs partner" style="left:472px;font-size:28px;letter-spacing:0"><span class="partner-mark square"></span>Keel Purse</div>
  <div class="abs cards">
    <span class="card">Veyra</span><span class="card">Tallycard</span><span class="card">Findway</span><span class="card">PalPost</span><span class="card">Riverstall</span><span class="card">Atlas Xpress</span>
  </div>
  <div class="abs footer-rule"></div>
  <p class="abs copyright">© copyrights 2022 &nbsp;CoinHarbor Rangers &nbsp;| &nbsp;All Rights Reserved</p>
</footer>

</body>
</html>
```